Business card for Northland's Blue Wagon.

Good day i am looking for a business card design for my business.
The name of the business is Northland's Blue Wagon. It is a van rental business that provides a driver and helper to the customer. Customer have use to van for small moves, studio or 1 bedroom, Moving furniture like couch or kitchen cabinets.
We are available evenings, weekends and holidays.
the means to contact us is by phone at 628-947-2071; By emails at Oakridge@northlandsbluewagon.net; or by social media, Facebook and Instagram.
You can see attached pictures of the van and or logo.

```html
<!DOCTYPE html>
<html lang="en">
<head>
<meta charset="utf-8">
<title>Northland's Blue Wagon – Business Card</title>
<link rel="stylesheet" href="https://fonts.googleapis.com/css2?family=Tinos:wght@400;700&display=swap">
<style>
  :root {
    --backdrop: #bcbdbf;
    --card-red: #d42027;
    --crest-dark: #a8171d;
    --crest-black: #1b1b1d;
    --card-white: #ffffff;
    --ink: #111111;
    --rule: #1a1a1a;
  }
  html, body {
    margin: 0;
    padding: 0;
    width: 1200px;
    height: 682px;
    overflow: hidden;
    background: var(--backdrop);
  }
  .presentation {
    display: block;
    width: 1200px;
    height: 682px;
    font-family: "Tinos", "Times New Roman", serif;
  }
  .side-label { font-size: 23px; fill: var(--ink); }
  .dimension-line { stroke: var(--ink); stroke-width: 1; fill: none; }
  .dimension-text { font-size: 18px; fill: var(--ink); }
  .card-front { fill: var(--card-white); }
  .card-back { fill: var(--card-red); }
  .crest-artwork { fill: url(#crest-tones); }
  .front-name { font-size: 24px; font-weight: 700; fill: var(--card-white); letter-spacing: 0.5px; }
  .back-title { font-size: 22.5px; font-weight: 700; fill: var(--card-white); }
  .back-tagline { font-size: 17.8px; fill: var(--card-white); }
  .back-contact { font-size: 13.5px; fill: var(--card-white); }
  .back-find { font-size: 13px; font-weight: 700; fill: var(--card-white); }
  .divider { stroke: var(--rule); stroke-width: 1; }
  .icon-disc { fill: var(--card-white); }
  .icon-mark { fill: var(--card-red); }
  .icon-line { stroke: var(--card-white); stroke-width: 1; fill: none; }
</style>
</head>
<body>
<svg class="presentation" viewBox="0 0 1200 682" xmlns="http://www.w3.org/2000/svg">
  <defs>
    <path id="card-outline" d="M0,0 C-55,45 -140,68 -205,62 C-220,60 -232,56 -239,52 C-225,72 -210,88 -200,104 C-190,125 -186,160 -182,200 C-178,245 -172,270 -165,285 L-165,321 L-140,335 A74,74 0 1 0 0,380 A74,74 0 1 0 140,335 L165,321 L165,285 C172,270 178,245 182,200 C186,160 190,125 200,104 C210,88 225,72 239,52 C232,56 220,60 205,62 C140,68 55,45 0,0 Z"/>
    <linearGradient id="crest-tones" x1="0" y1="0" x2="0" y2="1">
      <stop offset="0" stop-color="#d42027"/>
      <stop offset="0.55" stop-color="#a8171d"/>
      <stop offset="1" stop-color="#1b1b1d"/>
    </linearGradient>
  </defs>

  <!-- Side labels -->
  <text class="side-label" x="330" y="102" text-anchor="middle">Front</text>
  <text class="side-label" x="862" y="102" text-anchor="middle">Back</text>

  <!-- Dimensions -->
  <g class="dimensions">
    <line class="dimension-line" x1="53" y1="161" x2="53" y2="569"/>
    <line class="dimension-line" x1="49" y1="161" x2="57" y2="161"/>
    <line class="dimension-line" x1="49" y1="569" x2="57" y2="569"/>
    <text class="dimension-text" x="27" y="370" text-anchor="middle">3 in</text>
    <line class="dimension-line" x1="93" y1="631" x2="572" y2="631"/>
    <line class="dimension-line" x1="93" y1="627" x2="93" y2="635"/>
    <line class="dimension-line" x1="572" y1="627" x2="572" y2="635"/>
    <text class="dimension-text" x="332" y="652" text-anchor="middle">3.5 in</text>
  </g>

  <!-- Front of card -->
  <g class="card-face front" transform="translate(333,154)">
    <use href="#card-outline" class="card-front"/>
    <use href="#card-outline" class="crest-artwork" transform="translate(0,25) scale(0.86)"
         role="img" aria-label="Crest artwork area: shield with animals, leaf, laurels and wagon wheels"/>
    <text class="front-name" x="0" y="305" text-anchor="middle">Northland's Blue Wagon</text>
  </g>

  <!-- Back of card -->
  <g class="card-face back" transform="translate(867,154)">
    <use href="#card-outline" class="card-back"/>
  </g>

  <g class="back-content">
    <text class="back-title" x="867" y="255" text-anchor="middle">Van Rental Service with</text>
    <text class="back-title" x="867" y="281" text-anchor="middle">Driver &amp; Helper</text>

    <text class="back-tagline" x="867" y="320" text-anchor="middle">For small moves, studio or 1-bedroom</text>
    <text class="back-tagline" x="867" y="341" text-anchor="middle">apartments and furniture transport.</text>

    <!-- Phone -->
    <line class="divider" x1="681" y1="373" x2="853" y2="373"/>
    <line class="divider" x1="881" y1="373" x2="1053" y2="373"/>
    <circle class="icon-disc" cx="867" cy="373" r="7.5"/>
    <path class="icon-mark" d="M863.5,369 l1.6,-0.6 l1.1,2.1 l-1,0.8 c0.5,1.2 1.3,2 2.5,2.5 l0.8,-1 l2.1,1.1 l-0.6,1.6 c-3.6,0.1 -6.6,-2.9 -6.5,-6.5 z"/>
    <text class="back-contact" x="867" y="395" text-anchor="middle">628-947-2071</text>

    <!-- Email -->
    <line class="divider" x1="697" y1="423" x2="853" y2="423"/>
    <line class="divider" x1="881" y1="423" x2="1035" y2="423"/>
    <circle class="icon-disc" cx="867" cy="423" r="7.5"/>
    <rect class="icon-mark" x="862.5" y="419.8" width="9" height="6.4" rx="0.6"/>
    <path class="icon-line" d="M862.8,420.2 L867,423.6 L871.2,420.2"/>
    <text class="back-contact" x="867" y="444" text-anchor="middle">Oakridge@northlandsbluewagon.net</text>

    <!-- Social -->
    <text class="back-find" x="867" y="475" text-anchor="middle">Find us on</text>
    <line class="divider" x1="726" y1="489" x2="849" y2="489"/>
    <line class="divider" x1="885" y1="489" x2="1007" y2="489"/>
    <circle class="icon-disc" cx="858" cy="489" r="7.5"/>
    <circle class="icon-disc" cx="876" cy="489" r="7.5"/>
    <text class="back-contact" x="867" y="511" text-anchor="middle">Northland's Blue Wagon</text>
  </g>
</svg>
</body>
</html>
```